Clean Chic Simple Black & White One sided Biz Card

I need a business card for my company Brief Matter Arrangers. We are a luxury, white glove service for organizing files for attorneys.
I would like something that is stunningly simple and chic/sexy. This is going to be only one sided. We are going to use raised ink or ink embossing for the printing. So the logo will be raised in black. I am currently waiting to hear back from the printer as to whether or not the logo has to be in all black or can be left in its current state of black with grey initials. Please check our website for inspiration. www.briefmatterarrangers.example.
Thank you so much for your time.

* Please decide whichever title you think looks best(Chief Executive Officer, CEO, or President)
Updates

I really like the designs that make the logo large and the main focus.  
I also like the use of modern, masculine, simple, chic fonts for the slogan and info.

1) No bold font on slogan or info
2) Shrink info to be smaller maybe to make the logo bigger and more the focus
3) Maybe use grey for all the info and slogan so the focus will be on the logo

Thank you so much for your time!!

Target Market(s)

Luxury driven lawyers and their support staff

Industry/Entity Type

Printer

Requirements
Must have
• One sided card

Modern, sleek, masculine, chic, simple font.

Please add our slogan. Refer to file labeled "old logo" to see how we added our slogan under the old logo.
The slogan is, "We Set Method to the Counsel Record"

Please include the info below:
Marion Tullbeck (Chief Executive Officer, CEO, or President)
812 North Halvering Avenue, Suite 1400
Los Angeles, California 90071
P: (213)555-0182 F: (213)555-0167
mariont@briefmatterarrangers.example
www.briefmatterarrangers.example

Please refer to attached file labeled "inkpressingembossing requirements" for requirements from my printer. Thank you!
Nice to have
• It can be super simple with just the logo and my info. Or it could maybe have some cool feature. Just clean please.

I would prefer the info not be in bold. I think this will help the Logo stand out as the main focus.

I attached files of how the ink pressing and embossing will look.
Should not have
• No crazy shapes and no color other than black with a white background. The logo should be the focus since it will be embossed.

```html
<!DOCTYPE html>
<html lang="en">
<head>
<meta charset="utf-8">
<title>Brief Matter Arrangers – Business Card</title>
<link rel="stylesheet" href="https://fonts.googleapis.com/css2?family=Bodoni+Moda:opsz,wght@6..96,700&family=Cormorant+Garamond:ital,wght@0,400;1,400&display=swap">
<style>
  :root {
    --card-bg: #ffffff;
    --ink-black: #111111;
    --ink-grey: #9a9a9a;
  }
  html, body {
    margin: 0;
    padding: 0;
    overflow: hidden;
    background: var(--card-bg);
  }
  .card {
    position: relative;
    width: 1200px;
    height: 720px;
    background: var(--card-bg);
    overflow: hidden;
  }
  .brand-mark {
    position: absolute;
    left: 50%;
    top: 44px;
    width: 214px;
    height: 214px;
    margin-left: -107px;
  }
  .company-name {
    position: absolute;
    left: 0;
    right: 0;
    top: 276px;
    margin: 0;
    text-align: center;
    white-space: nowrap;
    font-family: "Bodoni Moda", "Didot", serif;
    font-weight: 700;
    font-size: 43px;
    line-height: 1.1;
    letter-spacing: 0.2em;
    color: var(--ink-black);
    text-transform: uppercase;
  }
  .slogan {
    position: absolute;
    left: 0;
    right: 0;
    top: 350px;
    margin: 0;
    text-align: center;
    white-space: nowrap;
    font-family: "Cormorant Garamond", "Garamond", serif;
    font-style: italic;
    font-variant: small-caps;
    font-size: 38px;
    line-height: 1.1;
    color: var(--ink-grey);
  }
  .contact {
    position: absolute;
    left: 0;
    right: 0;
    top: 500px;
    margin: 0;
    text-align: center;
    font-family: "Cormorant Garamond", "Garamond", serif;
    font-weight: 400;
    font-style: normal;
    color: var(--ink-grey);
  }
  .contact-name {
    display: block;
    font-variant: small-caps;
    font-size: 44px;
    line-height: 1;
    margin-bottom: 20px;
  }
  .contact-line {
    display: block;
    font-size: 34px;
    line-height: 1;
    margin-bottom: 22px;
    white-space: nowrap;
  }
</style>
</head>
<body>
  <main class="card">
    <svg class="brand-mark" viewBox="0 0 214 214" aria-hidden="true">
      <circle cx="107" cy="107" r="102" fill="none" stroke="var(--ink-grey)" stroke-width="4"/>
    </svg>

    <h1 class="company-name">Brief Matter Arrangers, Inc.</h1>
    <p class="slogan">“We Set Method to the Counsel Record”</p>

    <address class="contact">
      <span class="contact-name">Marion Tullbeck, CEO</span>
      <span class="contact-line">812 North Halvering Avenue, Suite 1400, Los Angeles, California 90071</span>
      <span class="contact-line">P: (213)555-0182 F: (213)555-0167 mariont@briefmatterarrangers.example</span>
    </address>
  </main>
</body>
</html>
```